Brightlane Photography
Sports & Dance Photography
Brightlane Photography - Photography
Creative Brief
Photography
Sports Leagues and Dance Schools
I have included an old brocure for sme reference material on our services. I would like trifold format
Marcotoledo Marcotoledo
Please download the asset file

```html
<!DOCTYPE html>
<html lang="en">
<head>
<meta charset="utf-8">
<title>Brightlane Photography Trifold</title>
<link rel="stylesheet" href="https://fonts.googleapis.com/css2?family=Oswald:wght@600;700&family=Open+Sans:wght@400;600&display=swap">
<style>
:root{
  --backdrop:#d9dadc;
  --paper:#ffffff;
  --pink:#e6217f;
  --navy:#1c2540;
  --yellow:#f7bb1e;
  --orange:#f7a21b;
  --green:#2f8a3c;
  --teal:#1fb0b4;
  --lime:#8cc63f;
  --ink:#3a3a3a;
  --photo-warm:#8a5a3c;
  --photo-dark:#2a2f45;
}
*{box-sizing:border-box;margin:0;padding:0}
html,body{width:1200px;height:799px;overflow:hidden;background:var(--backdrop)}
body{font-family:"Open Sans",Arial,sans-serif;color:var(--ink)}
.brochure{position:absolute;left:105px;top:16px;width:990px;height:766px;display:flex;background:var(--paper);box-shadow:0 4px 14px rgba(0,0,0,.18)}
.panel{position:relative;width:330px;height:766px;overflow:hidden;background:var(--paper)}
.panel + .panel{border-left:1px solid #e4e4e4}
.header-shape{position:absolute;left:0;top:0;width:330px}
.headline{position:absolute;left:24px;right:24px;font-family:"Oswald",Impact,sans-serif;font-weight:700;text-transform:uppercase;text-align:center;line-height:1.15;font-size:19px}
.headline.light{color:#fff}
.headline.gold{color:var(--yellow)}
.headline.navy{color:var(--navy)}
.headline.pink{color:var(--pink)}
.pill{position:absolute;left:50%;transform:translateX(-50%);padding:5px 22px;border-radius:16px;color:#fff;font-family:"Oswald",Impact,sans-serif;font-weight:600;font-size:15px;letter-spacing:.5px;text-transform:uppercase;white-space:nowrap}
.pill.pink{background:var(--pink)}
.pill.orange{background:var(--orange)}
.pill.teal{background:var(--teal)}
.pill.green{background:var(--green)}
.copy{position:absolute;left:28px;right:28px;font-size:11px;line-height:1.5;text-align:center}
.photo{position:absolute}
.band{position:absolute;left:0;width:330px}
</style>
</head>
<body>
<main class="brochure">

  <section class="panel panel-left">
    <svg class="header-shape" height="112" viewBox="0 0 330 112"><path d="M0 0H330V92Q165 122 0 92Z" fill="var(--pink)"/></svg>
    <h2 class="headline light" style="top:26px">Have you ever had lost orders or mistakes ?!</h2>
    <p class="copy" style="top:118px">Orders get lost when paper forms pass through many hands. Our system keeps every order safe from start to finish.</p>
    <div class="photo" style="left:28px;top:172px;width:274px;height:120px;background:linear-gradient(135deg,#5b4a3e,#b08a62)" role="img" aria-label="Photo of a portable photo printing station set up at an event"></div>
    <div class="pill pink" style="top:302px">Digital Ordering</div>
    <p class="copy" style="top:340px">Parents order online in minutes and every package is checked before it ships.</p>
    <h2 class="headline pink" style="top:392px">Have you been unable to make all your teams happy?</h2>
    <div class="pill orange" style="top:450px">Online Scheduling</div>
    <p class="copy" style="top:488px">Teams book their own picture day slots online, so every coach gets a time that works.</p>
    <div class="photo" style="left:0;top:580px;width:330px;height:186px;background:linear-gradient(180deg,#3d4a3a,#6d7a5c)" role="img" aria-label="Photo of a youth sports team posed in rows"></div>
  </section>

  <section class="panel panel-middle">
    <svg class="header-shape" height="132" viewBox="0 0 330 132"><path d="M0 0H330V108Q165 140 0 108Z" fill="var(--navy)"/></svg>
    <h2 class="headline gold" style="top:22px">Have you ever had customer service or been unable to get help?</h2>
    <div class="pill orange" style="top:122px">24 Hour Helpdesk</div>
    <p class="copy" style="top:166px">Our support team answers calls and messages day and night, all season long.</p>
    <div class="photo" style="left:0;top:222px;width:330px;height:222px;background:linear-gradient(180deg,#6b4a34,var(--photo-warm) 55%,#caa57a)" role="img" aria-label="Photo of a large dance squad posed in maroon and gold uniforms"></div>
    <svg class="band" style="top:430px" height="116" viewBox="0 0 330 116"><path d="M0 14Q165 -10 330 14V116H0Z" fill="var(--green)"/></svg>
    <h2 class="headline gold" style="top:462px">Do you still have photo packages left over from last season</h2>
    <p class="copy" style="top:554px">We offer flexible packages sized for each league, so nothing goes to waste.</p>
    <div class="photo" style="left:0;top:608px;width:330px;height:158px;background:linear-gradient(135deg,#1f2b5a,#4a6ad0)" role="img" aria-label="Photo of dancers performing on a blue lit stage"></div>
  </section>

  <section class="panel panel-right">
    <svg class="header-shape" height="132" viewBox="0 0 330 132"><path d="M0 0H330V108Q165 140 0 108Z" fill="var(--yellow)"/></svg>
    <h2 class="headline navy" style="top:20px">Give the people what they want. Awesome products that make every person want to buy!</h2>
    <div class="pill teal" style="top:124px">Awesome Products</div>
    <div class="photo" style="left:24px;top:170px;width:136px;height:118px;background:linear-gradient(135deg,#c0392b,#e8b04a)" role="img" aria-label="Photo of printed sports photo products and banners"></div>
    <p class="copy" style="left:172px;right:24px;top:186px;text-align:left">From banners to keepsake plaques, our prints are made to be shown off.</p>
    <svg class="band" style="top:300px" height="110" viewBox="0 0 330 110"><path d="M0 16Q165 -12 330 16V94Q165 122 0 94Z" fill="var(--teal)"/></svg>
    <h2 class="headline light" style="top:326px">Have you had a hard time finding a tournament photography expert?</h2>
    <div class="pill green" style="top:414px">Tournaments</div>
    <p class="copy" style="top:454px">Our crews cover every court and field at large events, with fast onsite printing.</p>
    <div class="band" style="top:510px;height:256px;background:var(--lime)"></div>
    <div class="photo" style="left:16px;top:524px;width:144px;height:170px;background:linear-gradient(180deg,#1d2340,#3b4d8c)" role="img" aria-label="Photo of athletes competing at a tournament"></div>
    <div class="photo" style="left:170px;top:524px;width:144px;height:170px;background:linear-gradient(180deg,#2a1a1a,#9b2b2b)" role="img" aria-label="Photo of a team celebrating at a tournament venue"></div>
  </section>

</main>
</body>
</html>
```